Two Web Banners Needed for children product website! Fun and colorful!

My website is www.brightpebbletrinkets.com.au

I want 2 banners for the home page.

Size: 1920x1080px

Colors I like:
#BBA5D0
#FBF5BC
#F2BBAD

Text:
1) We create unique and meaningful gifts
2) We help you create happy memories

Fonts: provided in link

Brief:
1) I need two banners that showcase my two products on my website. I have images and fonts are included you can use in the files.
2) I want to capture child nature, friendliness and happiness.
3) I have also included samples of what I like
4) It's important to use some of the customer photographs too

Link to files:
https://filedrop-example.net/downloads/a1b2c3d4e5f60718293a4b5c6d7e8f9020220101000000/0f1e2d3c4b5a69788796a5b4c3d2e1f020220101000001/9z8y7x

If link does not work please PM me

Target Market(s)

Parents of children

Industry/Entity Type

Children ecommerce

Font styles to use
Other font styles liked:
• in file

Requirements
Must have
• Clean modern look

```html
<!DOCTYPE html>
<html lang="en">
<head>
<meta charset="utf-8">
<title>Heirloom Seat Banner</title>
<link href="https://fonts.googleapis.com/css2?family=Baloo+2:wght@600;700&family=Montserrat:wght@800;900&family=Quicksand:wght@400;500&display=swap" rel="stylesheet">
<style>
  :root {
    --lavender: #BBA5D0;
    --lavender-deep: #B39CCB;
    --lavender-mist: #F2EEF6;
    --cream: #FBF5BC;
    --peach: #F2BBAD;
    --white: #FFFFFF;
  }
  * { margin: 0; padding: 0; box-sizing: border-box; }
  html, body { width: 1200px; height: 640px; overflow: hidden; background: var(--white); }
  .banner {
    position: relative;
    width: 1200px;
    height: 640px;
    overflow: hidden;
    background: var(--white);
  }
  .hero {
    position: absolute; left: 0; top: 0; width: 1200px; height: 494px;
    background: linear-gradient(180deg, #B9A5D0 0%, #C9B8DC 45%, var(--lavender-mist) 100%);
  }
  .eyebrow {
    position: absolute; left: 69px; top: 96px; width: 301px; height: 37px;
    background: var(--peach);
    color: var(--white);
    font-family: "Quicksand", sans-serif; font-weight: 500;
    font-size: 30px; letter-spacing: 4px;
    text-align: center; line-height: 39px;
  }
  .headline {
    position: absolute; left: 71px;
    color: var(--white);
    font-family: "Montserrat", sans-serif; font-weight: 800;
    font-size: 40px; letter-spacing: 3px; line-height: 1;
    text-shadow: 0 2px 4px rgba(120, 90, 150, 0.35);
    white-space: nowrap;
  }
  .headline--one { top: 144px; }
  .headline--two { top: 200px; }
  .gift-word {
    position: absolute; left: 70px; top: 242px; width: 310px; height: 100px;
  }
  .gift-word text {
    font-family: "Montserrat", sans-serif; font-weight: 900;
    font-size: 112px; letter-spacing: 12px;
    fill: var(--lavender-deep);
    stroke: var(--white); stroke-width: 8px; paint-order: stroke;
  }
  .offer-bar {
    position: absolute; left: 150px; top: 390px; width: 220px; height: 48px;
    background: var(--cream);
    color: var(--lavender);
    font-family: "Baloo 2", sans-serif; font-weight: 700;
    font-size: 17px; letter-spacing: 1.2px;
    line-height: 50px; padding-left: 26px;
    white-space: nowrap;
  }
  .offer-badge {
    position: absolute; left: 56px; top: 354px; width: 112px; height: 112px;
  }
  .offer-badge text {
    font-family: "Baloo 2", sans-serif; font-weight: 700;
    font-size: 27px; fill: var(--cream); letter-spacing: 1px;
  }
  .product-photo {
    position: absolute; left: 459px; top: 97px; width: 680px; height: 387px;
    border-radius: 10px;
    background: linear-gradient(100deg, #C7A9D6 0%, #D9B8D8 35%, #F2B9CB 55%, #5B2AA6 75%, #B0144A 100%);
    opacity: 0.55;
  }
  .tagline-band {
    position: absolute; left: 0; top: 494px; width: 1200px; height: 97px;
    background: var(--lavender);
    text-align: center;
    font-family: "Baloo 2", sans-serif; font-weight: 700;
    font-size: 29px; letter-spacing: 2.2px; line-height: 37px;
    padding-top: 10px;
    white-space: nowrap;
  }
  .tagline-band .question { color: var(--white); }
  .tagline-band .answer { color: var(--cream); }
</style>
</head>
<body>
  <main class="banner">
    <section class="hero">
      <div class="eyebrow">WE CREATE</div>
      <h1>
        <span class="headline headline--one">UNIQUE AND</span>
        <span class="headline headline--two">MEANINGFUL</span>
      </h1>
      <svg class="gift-word" viewBox="0 0 310 100" aria-label="GIFT">
        <text x="4" y="88">GIFT</text>
      </svg>

      <div class="offer-bar">On “Heirloom Seat”</div>
      <svg class="offer-badge" viewBox="0 0 112 112" aria-label="20% off">
        <g fill="var(--peach)">
          <circle cx="56" cy="56" r="46"/>
          <circle cx="56" cy="12" r="12"/><circle cx="78" cy="18" r="12"/>
          <circle cx="94" cy="34" r="12"/><circle cx="100" cy="56" r="12"/>
          <circle cx="94" cy="78" r="12"/><circle cx="78" cy="94" r="12"/>
          <circle cx="56" cy="100" r="12"/><circle cx="34" cy="94" r="12"/>
          <circle cx="18" cy="78" r="12"/><circle cx="12" cy="56" r="12"/>
          <circle cx="18" cy="34" r="12"/><circle cx="34" cy="18" r="12"/>
        </g>
        <g transform="rotate(-28 56 56)">
          <text x="56" y="52" text-anchor="middle">20%</text>
          <text x="60" y="80" text-anchor="middle">OFF</text>
        </g>
      </svg>

      <div class="product-photo" role="img" aria-label="Photo of three personalised children's chairs in lilac, purple and red with embroidered names, and a baby in a pink bodysuit sitting in front"></div>
    </section>

    <section class="tagline-band">
      <p class="question">Know someone who is about to become a parent?</p>
      <p class="answer">Why not give them “Heirloom Seat” that will last a lifetime</p>
    </section>
  </main>
</body>
</html>
```